Flyer for Custom Home Builder!

my company is Harlow Ridge Homes, I am looking for a flyer that we can send via email to a customer, or print and hand out. I am thinking four pages so we could print this and fold it., possibly creating a folder. The name of the company is Harlow Ridge Homes our website is here www.harlowridgehomes-example.com. Some text you can use "Crafting luxury homes isn't just a job, it's our passion.
With meticulous attention to detail and an unwavering commitment to using the finest materials, Harlow Ridge Homes consistently delivers exceptional results that stand as a testament to our commitment to quality."

"Trust is the cornerstone of our foundation.
With a proven track record of delivering on our promises for over 16 years, we prioritize transparent communication and integrity throughout every step of the home-building journey".

you may need to obtain the photos here
https://files.example-share.net/f/k27pw4m8zrt03xq61bnv/h?key=48vn2c9q1x7mb5t0ekd3h&dl=0

Target Market(s)

We build homes for every wealthy clients, therefore the photos are extremely important

Industry/Entity Type

Construction.

Requirements
Must have
• clear larger photos

```html
<!DOCTYPE html>
<html lang="en">
<head>
<meta charset="utf-8">
<title>Harlow Ridge Homes Flyer</title>
<link rel="stylesheet" href="https://fonts.googleapis.com/css2?family=Montserrat:wght@400;500;600;700;800;900&display=swap">
<style>
  :root{
    --page:#f2f2f2;
    --white:#ffffff;
    --charcoal:#2f3033;
    --charcoal-deep:#232427;
    --yellow:#f4d21f;
    --ink:#1d1d1f;
    --muted:#d6d6d6;
  }
  *{margin:0;padding:0;box-sizing:border-box}
  html,body{width:674px;height:1200px;overflow:hidden;background:var(--page)}
  body{font-family:"Montserrat",Arial,sans-serif;position:relative}
  .flyer{position:absolute;left:17px;top:143px;width:640px;height:914px;background:var(--charcoal);overflow:hidden;box-shadow:0 2px 10px rgba(0,0,0,.12)}
  .header{position:absolute;left:0;top:0;width:640px;height:222px;background:var(--white)}
  .brand{position:absolute;left:34px;top:58px;display:flex;flex-direction:column;gap:4px}
  .brand-name{font-weight:800;font-size:27px;letter-spacing:2px;color:var(--charcoal)}
  .brand-sub{font-weight:600;font-size:11px;letter-spacing:4px;color:var(--charcoal)}
  .hero-photo{position:absolute;left:290px;top:0;width:350px;height:370px;background:linear-gradient(180deg,#8fa4b6 0%,#c9d3db 40%,#e8e8e6 62%,#6b6a66 100%)}
  .intro{position:absolute;left:0;top:222px;width:640px;height:128px;background:var(--yellow)}
  .intro-title{position:absolute;left:34px;top:18px;width:250px;font-weight:900;font-size:23px;line-height:1.08;color:var(--ink);text-transform:uppercase}
  .intro-copy{position:absolute;left:34px;top:370px;width:262px;font-size:10.5px;line-height:1.5;font-weight:500;color:var(--white)}
  .gallery{position:absolute;left:330px;top:370px;width:280px;display:flex;flex-direction:column;gap:8px}
  .gallery .photo{width:280px;height:108px}
  .photo.kitchen{background:linear-gradient(135deg,#f3f1ec,#c9c4bb 60%,#6e6a63)}
  .photo.living{background:linear-gradient(135deg,#e7e2d8,#b7a58a 55%,#4d4a45)}
  .photo.bath{background:linear-gradient(135deg,#eeeeec,#bfbcb6 55%,#7d6a52)}
  .trust{position:absolute;left:34px;top:500px;width:270px}
  .trust-lead{font-weight:900;font-size:50px;line-height:1;color:var(--yellow);text-transform:uppercase}
  .trust-sub{margin-top:6px;font-weight:800;font-size:19px;line-height:1.12;color:var(--white);text-transform:uppercase}
  .trust-copy{position:absolute;left:34px;top:672px;width:262px;font-size:10.5px;line-height:1.5;font-weight:600;color:var(--white)}
  .contact-bar{position:absolute;left:0;top:840px;width:640px;height:74px;background:var(--charcoal-deep);display:flex;align-items:center;justify-content:space-between;padding:0 34px}
  .phone{display:flex;align-items:center;gap:10px;font-weight:800;font-size:22px;color:var(--white)}
  .details{display:flex;flex-direction:column;gap:6px;font-size:8.5px;font-weight:500;color:var(--muted);text-align:left}
  .details span{display:flex;align-items:center;gap:6px}
  .dot{width:7px;height:7px;border-radius:50%;background:var(--yellow);flex:none}
</style>
</head>
<body>
  <main class="flyer">
    <header class="header">
      <div class="brand">
        <span class="brand-name">HARLOW RIDGE</span>
        <span class="brand-sub">HOMES</span>
      </div>
    </header>

    <section class="intro">
      <h1 class="intro-title">Crafting luxury homes isn't just a job it's our passion</h1>
    </section>

    <div class="hero-photo" role="img" aria-label="Modern two-storey luxury home exterior at dusk"></div>

    <p class="intro-copy">With meticulous attention to detail and an unwavering commitment to using the finest materials, Harlow Ridge Homes consistently delivers exceptional results that stand as a testament to our commitment to quality.</p>

    <div class="gallery">
      <div class="photo kitchen" role="img" aria-label="Bright modern kitchen with island"></div>
      <div class="photo living" role="img" aria-label="Open living room with large windows"></div>
      <div class="photo bath" role="img" aria-label="Luxury bathroom with wood vanity"></div>
    </div>

    <section class="trust">
      <h2 class="trust-lead">Trust is</h2>
      <p class="trust-sub">The cornerstone of our foundation</p>
    </section>

    <p class="trust-copy">With a proven track record of delivering on our promises for over 16 years, we prioritize transparent communication and integrity throughout every step of the home-building journey</p>

    <footer class="contact-bar">
      <div class="phone">
        <svg width="26" height="26" viewBox="0 0 24 24" aria-hidden="true">
          <circle cx="12" cy="12" r="12" fill="#f4d21f"/>
          <path d="M8.6 6.5l1.6-.3 1.1 2.6-1.2 1c.6 1.4 1.7 2.5 3.1 3.1l1-1.2 2.6 1.1-.3 1.6c-.1.6-.7 1-1.3 1-3.9-.3-7-3.4-7.3-7.3 0-.6.4-1.2 1-1.3z" fill="#232427"/>
        </svg>
        (555) 014-2287
      </div>
      <div class="details">
        <span><i class="dot"></i>410 Cedar Bluff Lane, Suite 12, Austin TX 78700</span>
        <span><i class="dot"></i>www.harlowridgehomes-example.com</span>
      </div>
    </footer>
  </main>
</body>
</html>
```